Innovative IT Service Provider seeks engaging overview presentation to capture new business

*Please see attached Creative Brief for full details*

Overall Goals
The goal of this presentation is to provide new, prospective clients with an introduction to Harborline Systems, the services we provide, and what makes us a unique and superior choice for their IT Services. The deck should be able to clearly relay this information while clients review it on their own, without further explanation from a company representative.

Design Goals
We are looking for a professional, modern, streamlined, sleek design that reflects our status as a leader in information technology and innovation.

Company Overview
As an IT Managed Service Provider, companies choose to outsource some or all of their internal IT functions to us to take advantage of our many areas of expertise and so they can focus on their core business, whatever industry they may be in. We also specialize in IT Cyber Security and Consulting, always providing our clients with thought leadership and insight into the latest IT innovations. We ultimately find ways to deliver value to our clients through our various IT solutions.

```html
<!DOCTYPE html>
<html lang="en">
<head>
<meta charset="utf-8">
<title>Harborline Systems – Company Overview</title>
<link rel="stylesheet" href="https://fonts.googleapis.com/css2?family=Montserrat:wght@600;700&family=Roboto:wght@400;500;700&family=Rubik:wght@600;700&family=Playfair+Display:wght@700&display=swap">
<style>
:root{
  --navy:#1f3a72;
  --navy-dark:#16295a;
  --red:#b3141d;
  --title-red:#9e1f2c;
  --gap:#8d8d8d;
  --ink:#2a2a2a;
  --white:#ffffff;
  --soft:#eef1f6;
}
*{box-sizing:border-box;margin:0;padding:0}
html,body{width:1200px;height:4310px;overflow:hidden;background:var(--gap)}
body{position:relative;font-family:Roboto,Arial,sans-serif;color:var(--ink)}
.slide{position:absolute;left:0;width:1200px;overflow:hidden;background:var(--white)}
.abs{position:absolute}
.brand{position:absolute;display:flex;align-items:center;gap:18px;font-family:Montserrat,Arial,sans-serif;font-weight:700;color:var(--navy);letter-spacing:2px;line-height:1.05}
.brand-mark{background:var(--navy);flex:none}
.topbar{position:absolute;left:0;top:0;width:1200px;height:72px;background:var(--red)}
.corner{position:absolute;left:0;top:72px}
.contact{position:absolute;display:flex;align-items:center;gap:18px;color:var(--white);font-family:Montserrat,Arial,sans-serif;font-weight:700;font-size:14px;letter-spacing:.5px}
.contact .link{text-decoration:underline}
.ico{width:34px;height:34px;border-radius:50%;background:var(--white);display:flex;align-items:center;justify-content:center;flex:none}
.pagenum{position:absolute;width:34px;height:34px;border-radius:50%;background:var(--white);border:3px solid var(--red);color:var(--red);font:700 14px Roboto,Arial,sans-serif;display:flex;align-items:center;justify-content:center;right:32px}
.photo{position:absolute}
.section-title{position:absolute;left:0;width:1200px;text-align:center;font-family:Rubik,Arial,sans-serif;font-weight:700;color:var(--title-red);font-size:31px;letter-spacing:.5px}
/* slide 2 */
.stat-tile{position:absolute;width:142px;height:114px;box-shadow:8px -6px 0 var(--red);display:flex;align-items:center;justify-content:center}
.stat-tile.navy{background:var(--navy)}
.stat-tile.light{background:var(--white);border:1px solid #d6d6d6}
.stat-caption{position:absolute;width:210px;text-align:center;font-size:16px;line-height:1.35;color:#222}
.stat-caption b{color:var(--red);font-weight:700}
.industries-title{position:absolute;left:631px;top:390px;font:700 21px Roboto,Arial,sans-serif;color:#1a1a1a}
.industry{position:absolute;display:flex;align-items:center;gap:16px;font-size:15px;color:#222}
.bullet{width:18px;height:18px;border-radius:50%;background:var(--navy);display:flex;align-items:center;justify-content:center}
/* slide 3 */
.service{position:absolute;left:572px;width:436px;height:60px;display:flex}
.service .tag{width:64px;height:60px;background:var(--red);display:flex;align-items:center;justify-content:center}
.service .label{flex:1;background:var(--white);border:2px solid #d9d9d9;border-left:none;box-shadow:2px 3px 6px rgba(0,0,0,.18);display:flex;align-items:center;padding-left:36px;font:700 18px Roboto,Arial,sans-serif;color:#141414}
/* slide 4 */
.serif-title{position:absolute;left:0;width:1200px;text-align:center;font-family:"Playfair Display",Georgia,serif;font-weight:700;font-size:28px;color:var(--title-red);letter-spacing:1px}
.process{position:absolute;left:84px;width:446px;height:124px}
.process .panel{position:absolute;left:104px;top:28px;width:340px;height:70px;background:var(--white);box-shadow:2px 3px 8px rgba(0,0,0,.2);border-right:5px solid var(--navy);display:flex;align-items:center;justify-content:center;font:700 19px Roboto,Arial,sans-serif;color:#151515;padding-left:30px}
.process svg{position:absolute;left:0;top:0}
.dash{position:absolute;background:var(--white);border:2px solid var(--navy);box-shadow:3px 4px 10px rgba(0,0,0,.25);font-family:Roboto,Arial,sans-serif}
.dash .bar{height:12px;background:var(--navy-dark);color:#fff;font-size:9px;text-align:center;line-height:12px}
/* slide 5 */
.lead{position:absolute;left:240px;width:720px;text-align:center;font-size:15px;line-height:1.65;color:#222}
.ciso-list{position:absolute;left:96px;top:284px;list-style:none;width:460px}
.ciso-list li{position:relative;padding-left:36px;font-size:15px;line-height:38px;color:#222}
.ciso-list li::before{content:"";position:absolute;left:0;top:11px;width:17px;height:17px;border-radius:50%;background:var(--navy)}
.ciso-list li::after{content:"";position:absolute;left:5px;top:16px;width:4px;height:4px;border-right:2px solid #fff;border-top:2px solid #fff;transform:rotate(45deg)}
/* slide 6 */
.thanks{position:absolute;left:560px;width:460px;text-align:center;font:700 44px Rubik,Arial,sans-serif;color:var(--white);letter-spacing:1px}
.info{position:absolute;left:636px;display:flex;align-items:flex-start;gap:26px;font-size:15px;line-height:1.45;color:#222}
.info .link{font:700 14px Montserrat,Arial,sans-serif;color:var(--navy);text-decoration:underline}
</style>
</head>
<body>

<!-- ========== Slide 1: Cover ========== -->
<section class="slide" style="top:0;height:675px">
  <svg class="abs" style="left:0;top:0" width="1200" height="566" viewBox="0 0 1200 566">
    <path d="M610 0 C 600 240 720 470 1020 545 L1200 566 L1200 0 Z" fill="var(--red)"/>
    <path d="M650 0 C 650 230 760 440 1040 520 L1200 540 L1200 0 Z" fill="#0f4a63" role="img" aria-label="Photo of a laptop with a glowing padlock on a cyber security background"/>
    <path d="M650 0 C 650 230 760 440 1040 520 L1200 540 L1200 0 Z" fill="url(#coverGlow)"/>
    <defs>
      <radialGradient id="coverGlow" cx="0.7" cy="0.45" r="0.6">
        <stop offset="0" stop-color="#3fd3e0" stop-opacity=".75"/>
        <stop offset="1" stop-color="#06243a" stop-opacity=".9"/>
      </radialGradient>
    </defs>
  </svg>
  <div class="brand" style="left:96px;top:236px;font-size:44px;flex-direction:column;align-items:flex-start;gap:16px">
    <span class="brand-mark" style="width:64px;height:64px"></span>
    <span>HARBORLINE<br>SYSTEMS</span>
  </div>
  <svg class="abs" style="left:0;top:566px" width="1200" height="109" viewBox="0 0 1200 109">
    <path d="M0 0 H575 L600 44 L625 0 H1200 V109 H0 Z" fill="var(--navy)"/>
  </svg>
  <div class="contact" style="left:67px;top:616px">
    <span class="ico"><svg width="18" height="14" viewBox="0 0 18 14"><rect x="1" y="1" width="16" height="12" rx="1.5" fill="var(--navy)"/><path d="M1.5 2 L9 8 L16.5 2" stroke="#fff" stroke-width="1.6" fill="none"/></svg></span>
    <span class="link">HARBORLINESYSTEMS.COM</span>
  </div>
  <div class="contact" style="left:858px;top:619px">
    <span class="ico"><svg width="16" height="16" viewBox="0 0 24 24"><path d="M6.6 10.8a15 15 0 0 0 6.6 6.6l2.2-2.2a1 1 0 0 1 1-.25 11.4 11.4 0 0 0 3.6.57 1 1 0 0 1 1 1V20a1 1 0 0 1-1 1A17 17 0 0 1 3 4a1 1 0 0 1 1-1h3.5a1 1 0 0 1 1 1c0 1.25.2 2.45.57 3.57a1 1 0 0 1-.25 1z" fill="var(--navy)"/></svg></span>
    <span>+1 555 014 2290</span>
  </div>
  <div class="pagenum" style="top:616px;right:36px;border-color:var(--white);background:var(--white)">01</div>
</section>

<!-- ========== Slide 2: Service Introduction ========== -->
<section class="slide" style="top:711px;height:678px">
  <div class="photo" role="img" aria-label="Faded photo of a presenter addressing a seated audience" style="left:0;top:72px;width:1200px;height:606px;background:linear-gradient(180deg,#ffffff 0%,#f3f3f3 45%,#e4e3e1 100%);opacity:.95"></div>
  <div class="topbar"></div>
  <svg class="corner" width="70" height="90" viewBox="0 0 70 90"><path d="M0 0 H64 L0 88 Z" fill="var(--red)"/></svg>
  <div class="contact" style="left:72px;top:19px">
    <span class="ico"><svg width="18" height="14" viewBox="0 0 18 14"><rect x="1" y="1" width="16" height="12" rx="1.5" fill="var(--red)"/><path d="M1.5 2 L9 8 L16.5 2" stroke="#fff" stroke-width="1.6" fill="none"/></svg></span>
    <span class="link">HARBORLINESYSTEMS.COM</span>
  </div>
  <div class="contact" style="left:863px;top:19px">
    <span class="ico"><svg width="16" height="16" viewBox="0 0 24 24"><path d="M6.6 10.8a15 15 0 0 0 6.6 6.6l2.2-2.2a1 1 0 0 1 1-.25 11.4 11.4 0 0 0 3.6.57 1 1 0 0 1 1 1V20a1 1 0 0 1-1 1A17 17 0 0 1 3 4a1 1 0 0 1 1-1h3.5a1 1 0 0 1 1 1c0 1.25.2 2.45.57 3.57a1 1 0 0 1-.25 1z" fill="var(--red)"/></svg></span>
    <span>+1 555 014 2290</span>
  </div>

  <div class="section-title" style="top:116px">SERVICE INTRODUCTION</div>

  <div class="stat-tile navy" style="left:105px;top:206px">
    <svg width="60" height="56" viewBox="0 0 60 56" fill="none" stroke="#fff" stroke-width="2.4"><circle cx="30" cy="34" r="12"/><path d="M24 34l4 4 8-8"/><path d="M10 8l2 4 4 .5-3 3 1 4-4-2-4 2 1-4-3-3 4-.5z" fill="#fff" stroke="none"/><path d="M30 2l2 4 4 .5-3 3 1 4-4-2-4 2 1-4-3-3 4-.5z" fill="#fff" stroke="none"/><path d="M50 8l2 4 4 .5-3 3 1 4-4-2-4 2 1-4-3-3 4-.5z" fill="#fff" stroke="none"/></svg>
  </div>
  <div class="stat-caption" style="left:73px;top:334px"><b>25+ years</b> of IT Management Solutions Expertise</div>

  <div class="stat-tile navy" style="left:338px;top:206px">
    <svg width="66" height="58" viewBox="0 0 66 58" fill="none" stroke="#fff" stroke-width="2.4"><rect x="4" y="12" width="44" height="30" rx="2"/><path d="M20 42v8h12v-8M14 52h24"/><rect x="30" y="3" width="32" height="22" rx="2" fill="var(--navy)"/><path d="M43 10l7 4-7 4z" fill="#fff" stroke="none"/><path d="M10 20h16M10 26h16M10 32h10"/></svg>
  </div>
  <div class="stat-caption" style="left:305px;top:334px">More than <b>80,000 devices</b> under management Globally</div>

  <div class="stat-tile navy" style="left:120px;top:433px">
    <svg width="56" height="58" viewBox="0 0 56 58" fill="none" stroke="#fff" stroke-width="3"><path d="M10 30v-6a18 18 0 0 1 36 0v6"/><rect x="6" y="28" width="9" height="16" rx="3" fill="#fff"/><rect x="41" y="28" width="9" height="16" rx="3" fill="#fff"/><path d="M46 44c0 7-8 9-14 9"/><rect x="26" y="50" width="8" height="6" rx="2" fill="#fff" stroke="none"/></svg>
  </div>
  <div class="stat-caption" style="left:88px;top:557px">Service Desk handles over <b>7,500+ phone calls</b> a month and close to <b>20,000 tickets.</b></div>

  <div class="stat-tile light" style="left:335px;top:433px">
    <svg width="64" height="52" viewBox="0 0 64 52" fill="var(--navy)"><circle cx="14" cy="10" r="6"/><circle cx="32" cy="8" r="6"/><circle cx="50" cy="10" r="6"/><path d="M4 30c0-8 4-12 10-12s10 4 10 12zM22 28c0-8 4-12 10-12s10 4 10 12zM40 30c0-8 4-12 10-12s10 4 10 12z"/><path d="M12 40l10-8 10 6 10-6 10 8-12 10-8-6-8 6z"/></svg>
  </div>
  <div class="stat-caption" style="left:301px;top:557px">Partner to <b>Top 500</b> and mid-market companies</div>

  <div class="brand" style="left:604px;top:232px;font-size:40px">
    <span class="brand-mark" style="width:40px;height:40px"></span>
    <span>HARBORLINE<br>SYSTEMS</span>
  </div>

  <div class="industries-title">SERVING DIVERSE INDUSTRIES INCLUDING:</div>
  <div class="industry" style="left:632px;top:450px"><span class="bullet"><svg width="8" height="8" viewBox="0 0 8 8"><path d="M2 1l3 3-3 3" stroke="#fff" stroke-width="1.6" fill="none"/></svg></span>Non-Profit</div>
  <div class="industry" style="left:632px;top:486px"><span class="bullet"><svg width="8" height="8" viewBox="0 0 8 8"><path d="M2 1l3 3-3 3" stroke="#fff" stroke-width="1.6" fill="none"/></svg></span>Transportation &amp; Logistics</div>
  <div class="industry" style="left:632px;top:521px"><span class="bullet"><svg width="8" height="8" viewBox="0 0 8 8"><path d="M2 1l3 3-3 3" stroke="#fff" stroke-width="1.6" fill="none"/></svg></span>Financial &amp; Banking</div>
  <div class="industry" style="left:632px;top:558px"><span class="bullet"><svg width="8" height="8" viewBox="0 0 8 8"><path d="M2 1l3 3-3 3" stroke="#fff" stroke-width="1.6" fill="none"/></svg></span>Insurance</div>
  <div class="industry" style="left:877px;top:450px"><span class="bullet"><svg width="8" height="8" viewBox="0 0 8 8"><path d="M2 1l3 3-3 3" stroke="#fff" stroke-width="1.6" fill="none"/></svg></span>Healthcare</div>
  <div class="industry" style="left:877px;top:486px"><span class="bullet"><svg width="8" height="8" viewBox="0 0 8 8"><path d="M2 1l3 3-3 3" stroke="#fff" stroke-width="1.6" fill="none"/></svg></span>Manufacturing</div>
  <div class="industry" style="left:877px;top:521px"><span class="bullet"><svg width="8" height="8" viewBox="0 0 8 8"><path d="M2 1l3 3-3 3" stroke="#fff" stroke-width="1.6" fill="none"/></svg></span>Real Estate</div>
  <div class="industry" style="left:877px;top:558px"><span class="bullet"><svg width="8" height="8" viewBox="0 0 8 8"><path d="M2 1l3 3-3 3" stroke="#fff" stroke-width="1.6" fill="none"/></svg></span>And More</div>

  <div class="pagenum" style="top:604px">02</div>
</section>

<!-- ========== Slide 3: Services ========== -->
<section class="slide" style="top:1436px;height:677px">
  <div class="topbar"></div>
  <svg class="corner" width="70" height="90" viewBox="0 0 70 90"><path d="M0 0 H64 L0 88 Z" fill="var(--red)"/></svg>
  <div class="contact" style="left:72px;top:19px">
    <span class="ico"><svg width="18" height="14" viewBox="0 0 18 14"><rect x="1" y="1" width="16" height="12" rx="1.5" fill="var(--red)"/><path d="M1.5 2 L9 8 L16.5 2" stroke="#fff" stroke-width="1.6" fill="none"/></svg></span>
    <span class="link">HARBORLINESYSTEMS.COM</span>
  </div>
  <div class="contact" style="left:863px;top:19px">
    <span class="ico"><svg width="16" height="16" viewBox="0 0 24 24"><path d="M6.6 10.8a15 15 0 0 0 6.6 6.6l2.2-2.2a1 1 0 0 1 1-.25 11.4 11.4 0 0 0 3.6.57 1 1 0 0 1 1 1V20a1 1 0 0 1-1 1A17 17 0 0 1 3 4a1 1 0 0 1 1-1h3.5a1 1 0 0 1 1 1c0 1.25.2 2.45.57 3.57a1 1 0 0 1-.25 1z" fill="var(--red)"/></svg></span>
    <span>+1 555 014 2290</span>
  </div>

  <div class="abs" style="left:104px;top:156px;width:512px;height:446px;border:4px solid var(--red);border-radius:4px"></div>
  <div class="photo" role="img" aria-label="Photo of a professional working on a laptop in a server room" style="left:100px;top:162px;width:508px;height:446px;border:4px solid var(--navy);border-radius:4px;background:radial-gradient(circle at 65% 45%,#2f7fd9 0%,#12356e 45%,#0a1530 100%)"></div>

  <div class="service" style="top:199px"><span class="tag"><svg width="32" height="32" viewBox="0 0 32 32" fill="#fff"><circle cx="16" cy="10" r="7"/><circle cx="16" cy="10" r="3" fill="var(--red)"/><path d="M3 22h6l6 3h8l6-4v3l-7 5H12l-9-3z"/></svg></span><span class="label">Managed Services</span></div>
  <div class="service" style="top:293px"><span class="tag"><svg width="32" height="32" viewBox="0 0 32 32" fill="none" stroke="#fff" stroke-width="2"><circle cx="16" cy="8" r="4"/><circle cx="7" cy="18" r="3"/><circle cx="25" cy="18" r="3"/><path d="M10 30c0-5 3-8 6-8s6 3 6 8M2 30c0-3 2-6 5-6M30 30c0-3-2-6-5-6M16 12v6"/></svg></span><span class="label">Professional Services</span></div>
  <div class="service" style="top:387px"><span class="tag"><svg width="32" height="32" viewBox="0 0 32 32" fill="#fff"><circle cx="13" cy="8" r="3.5"/><circle cx="21" cy="8" r="3.5"/><path d="M7 18c0-4 3-6 6-6s6 2 6 6zM15 18c0-4 3-6 6-6s6 2 6 6z"/><path d="M2 22h6l6 3h8l8-5v3l-8 6H12l-10-3z"/></svg></span><span class="label">Staffing Services</span></div>
  <div class="service" style="top:481px"><span class="tag"><svg width="32" height="32" viewBox="0 0 32 32" fill="none" stroke="#fff" stroke-width="2.2"><path d="M2 5h4l4 15h14l3-10H8"/><circle cx="12" cy="26" r="2" fill="#fff"/><circle cx="22" cy="26" r="2" fill="#fff"/><circle cx="25" cy="22" r="4"/></svg></span><span class="label">Procurement Services</span></div>

  <div class="pagenum" style="top:610px">03</div>
</section>

<!-- ========== Slide 4: Why HS ========== -->
<section class="slide" style="top:2176px;height:692px">
  <div class="topbar"></div>
  <svg class="corner" width="70" height="90" viewBox="0 0 70 90"><path d="M0 0 H64 L0 88 Z" fill="var(--red)"/></svg>
  <div class="contact" style="left:72px;top:19px">
    <span class="ico"><svg width="18" height="14" viewBox="0 0 18 14"><rect x="1" y="1" width="16" height="12" rx="1.5" fill="var(--red)"/><path d="M1.5 2 L9 8 L16.5 2" stroke="#fff" stroke-width="1.6" fill="none"/></svg></span>
    <span class="link">HARBORLINESYSTEMS.COM</span>
  </div>
  <div class="contact" style="left:863px;top:19px">
    <span class="ico"><svg width="16" height="16" viewBox="0 0 24 24"><path d="M6.6 10.8a15 15 0 0 0 6.6 6.6l2.2-2.2a1 1 0 0 1 1-.25 11.4 11.4 0 0 0 3.6.57 1 1 0 0 1 1 1V20a1 1 0 0 1-1 1A17 17 0 0 1 3 4a1 1 0 0 1 1-1h3.5a1 1 0 0 1 1 1c0 1.25.2 2.45.57 3.57a1 1 0 0 1-.25 1z" fill="var(--red)"/></svg></span>
    <span>+1 555 014 2290</span>
  </div>

  <div class="serif-title" style="top:134px">WHY HS? PROCESS DRIVEN</div>

  <div class="process" style="top:221px">
    <div class="panel">BUSINESS ANALYTICS</div>
    <svg width="124" height="124" viewBox="0 0 124 124"><polygon points="62,4 114,33 114,91 62,120 10,91 10,33" fill="#fff" stroke="var(--red)" stroke-width="4"/><polygon points="62,16 103,39 103,85 62,108 21,85 21,39" fill="#f6e9ea"/><rect x="44" y="44" width="38" height="28" fill="none" stroke="var(--navy)" stroke-width="3"/><path d="M50 64l8-8 6 5 12-10" stroke="var(--red)" stroke-width="3" fill="none"/><circle cx="46" cy="74" r="8" fill="none" stroke="var(--navy)" stroke-width="3"/><path d="M40 80l-6 7" stroke="var(--navy)" stroke-width="3"/></svg>
  </div>
  <div class="process" style="top:365px">
    <div class="panel">TREND ANALYSIS</div>
    <svg width="124" height="124" viewBox="0 0 124 124"><polygon points="62,4 114,33 114,91 62,120 10,91 10,33" fill="#fff" stroke="var(--red)" stroke-width="4"/><polygon points="62,16 103,39 103,85 62,108 21,85 21,39" fill="#f6e9ea"/><path d="M40 82h46M40 82V42" stroke="var(--navy)" stroke-width="3"/><rect x="46" y="66" width="7" height="14" fill="var(--navy)"/><rect x="57" y="58" width="7" height="22" fill="var(--navy)"/><rect x="68" y="62" width="7" height="18" fill="var(--navy)"/><rect x="79" y="50" width="7" height="30" fill="var(--navy)"/><path d="M46 58l12-10 10 6 16-14" stroke="var(--red)" stroke-width="3" fill="none"/></svg>
  </div>
  <div class="process" style="top:509px">
    <div class="panel">CONTINUOUS IMPROVEMENT</div>
    <svg width="124" height="124" viewBox="0 0 124 124"><polygon points="62,4 114,33 114,91 62,120 10,91 10,33" fill="#fff" stroke="var(--red)" stroke-width="4"/><polygon points="62,16 103,39 103,85 62,108 21,85 21,39" fill="#f6e9ea"/><path d="M42 56a22 22 0 0 1 38-8M82 68a22 22 0 0 1-38 8" stroke="var(--navy)" stroke-width="3" fill="none"/><path d="M80 40v9h-9M44 84v-9h9" stroke="var(--navy)" stroke-width="3" fill="none"/><rect x="52" y="62" width="5" height="10" fill="var(--red)"/><rect x="60" y="56" width="5" height="16" fill="var(--red)"/><rect x="68" y="50" width="5" height="22" fill="var(--red)"/></svg>
  </div>

  <!-- dashboard panels -->
  <div class="dash" style="left:636px;top:285px;width:388px;height:198px">
    <div class="bar">Calls</div>
    <svg width="384" height="182" viewBox="0 0 384 182">
      <circle cx="46" cy="52" r="22" fill="none" stroke="#d8dde8" stroke-width="8"/><path d="M46 30a22 22 0 0 1 20 30" fill="none" stroke="var(--navy)" stroke-width="8"/>
      <text x="46" y="56" font-size="11" text-anchor="middle" fill="#555">200%</text>
      <text x="14" y="104" font-size="8" fill="#777">Answered Rate</text>
      <text x="14" y="140" font-size="18" fill="#222">15</text>
      <rect x="92" y="24" width="40" height="150" fill="#eef1f6"/>
    </svg>
  </div>
  <div class="dash" style="left:723px;top:335px;width:368px;height:187px">
    <div class="bar" style="background:#fff;color:#555"></div>
    <svg width="364" height="171" viewBox="0 0 364 171">
      <rect x="6" y="2" width="88" height="14" fill="var(--navy-dark)"/><text x="50" y="12" font-size="9" text-anchor="middle" fill="#fff">Survey Results</text>
      <text x="130" y="30" font-size="14" fill="#222">4.65</text><text x="175" y="30" font-size="8" fill="#777">Avg Score</text>
      <text x="230" y="30" font-size="14" fill="#222">33</text>
      <rect x="270" y="6" width="88" height="8" fill="#9bb7df"/><rect x="270" y="16" width="88" height="8" fill="#c9d8ee"/><rect x="270" y="26" width="88" height="8" fill="#9bb7df"/>
      <text x="8" y="142" font-size="14" fill="#222">99.50%</text><text x="8" y="156" font-size="8" fill="#777">SLA Met</text>
    </svg>
  </div>
  <div class="dash" style="left:787px;top:385px;width:335px;height:186px">
    <svg width="331" height="182" viewBox="0 0 331 182">
      <text x="10" y="16" font-size="8" fill="#777">Open Tickets</text>
      <rect x="40" y="34" width="10" height="60" fill="var(--navy)"/><rect x="40" y="94" width="10" height="10" fill="var(--red)"/>
      <rect x="80" y="30" width="70" height="70" fill="#eef1f6"/>
      <rect x="178" y="30" width="140" height="40" fill="#eef1f6"/><rect x="230" y="52" width="40" height="8" fill="#3a6fc4"/>
      <circle cx="72" cy="142" r="26" fill="var(--navy)"/><path d="M72 142V116a26 26 0 0 1 24 16z" fill="var(--red)"/><path d="M72 142l24-10a26 26 0 0 1-6 28z" fill="#3fa0d8"/>
      <circle cx="226" cy="142" r="26" fill="#e58a8a"/><path d="M226 142V116a26 26 0 0 1 22 38z" fill="#4a7bd0"/><path d="M226 142l22 12a26 26 0 0 1-30 12z" fill="var(--red)"/>
    </svg>
  </div>

  <div class="pagenum" style="top:628px">04</div>
</section>

<!-- ========== Slide 5: v-CISO ========== -->
<section class="slide" style="top:2916px;height:676px;background:linear-gradient(180deg,#e9edf3 0%,#f4f6f9 55%,#e6ebf2 100%)">
  <div class="topbar"></div>
  <svg class="corner" width="70" height="90" viewBox="0 0 70 90"><path d="M0 0 H64 L0 88 Z" fill="var(--red)"/></svg>
  <div class="contact" style="left:72px;top:19px">
    <span class="ico"><svg width="18" height="14" viewBox="0 0 18 14"><rect x="1" y="1" width="16" height="12" rx="1.5" fill="var(--red)"/><path d="M1.5 2 L9 8 L16.5 2" stroke="#fff" stroke-width="1.6" fill="none"/></svg></span>
    <span class="link">HARBORLINESYSTEMS.COM</span>
  </div>
  <div class="contact" style="left:863px;top:19px">
    <span class="ico"><svg width="16" height="16" viewBox="0 0 24 24"><path d="M6.6 10.8a15 15 0 0 0 6.6 6.6l2.2-2.2a1 1 0 0 1 1-.25 11.4 11.4 0 0 0 3.6.57 1 1 0 0 1 1 1V20a1 1 0 0 1-1 1A17 17 0 0 1 3 4a1 1 0 0 1 1-1h3.5a1 1 0 0 1 1 1c0 1.25.2 2.45.57 3.57a1 1 0 0 1-.25 1z" fill="var(--red)"/></svg></span>
    <span>+1 555 014 2290</span>
  </div>

  <div class="section-title" style="top:104px">V-CISO SERVICES</div>
  <p class="lead" style="top:164px">Comprehensive security leadership and program oversight made available for companies of all sizes. HS has over 20 years of experience managing security programs and consulting with Top 500 companies.</p>

  <ul class="ciso-list">
    <li>Enterprise Compliance and Risk Management focus</li>
    <li>Security standards and framework selection, gap analysis and implementation</li>
    <li>Security policy, process, and procedure development and implementation</li>
    <li>Information security leadership and guidance</li>
    <li>Security posture assessment</li>
    <li>Ongoing security compliance management</li>
    <li>Internal audit support</li>
  </ul>

  <div class="abs" style="left:604px;top:250px;width:502px;height:364px;border:4px solid var(--navy)"></div>
  <div class="photo" role="img" aria-label="Illustration of a hand touching a glowing security shield interface" style="left:598px;top:256px;width:498px;height:360px;background:radial-gradient(circle at 45% 50%,#4fa4ff 0%,#163f9a 40%,#0a1a4a 100%);border:4px solid #fff"></div>

  <div class="pagenum" style="top:605px">05</div>
</section>

<!-- ========== Slide 6: Thank you ========== -->
<section class="slide" style="top:3643px;height:667px;background:var(--navy)">
  <svg class="abs" style="left:0;top:0" width="1200" height="667" viewBox="0 0 1200 667">
    <path d="M0 330 C 180 300 320 420 520 410 C 720 400 760 330 960 330 C 1080 330 1150 360 1200 370 V667 H0 Z" fill="var(--red)"/>
    <path d="M0 360 C 180 330 330 450 530 440 C 730 430 780 360 970 362 C 1090 364 1160 392 1200 400 V667 H0 Z" fill="var(--white)"/>
    <path d="M0 250 C 200 250 360 330 450 450 C 500 520 510 600 505 667 H0 Z" fill="#a9b3c3" role="img" aria-label="Photo of two business people shaking hands in an office"/>
    <path d="M0 250 C 200 250 360 330 450 450 C 500 520 510 600 505 667 H0 Z" fill="url(#handshake)"/>
    <defs><linearGradient id="handshake" x1="0" y1="0" x2="1" y2="1"><stop offset="0" stop-color="#dfe4ec"/><stop offset="1" stop-color="#6b778c"/></linearGradient></defs>
  </svg>

  <div class="brand" style="left:396px;top:104px;font-size:44px;color:var(--white)">
    <span class="brand-mark" style="width:48px;height:48px;background:var(--white)"></span>
    <span>HARBORLINE<br>SYSTEMS</span>
  </div>
  <div class="thanks" style="top:276px">THANK YOU !!!</div>

  <div class="info" style="top:458px;left:634px">
    <svg width="18" height="22" viewBox="0 0 18 22"><path d="M9 1a7 7 0 0 1 7 7c0 5-7 13-7 13S2 13 2 8a7 7 0 0 1 7-7z" fill="var(--navy)"/><circle cx="9" cy="8" r="2.6" fill="#fff"/></svg>
    <span>Harborline Systems, 48 Quay Street<br>AP-204518</span>
  </div>
  <div class="info" style="top:535px;left:634px">
    <svg width="18" height="18" viewBox="0 0 24 24"><path d="M6.6 10.8a15 15 0 0 0 6.6 6.6l2.2-2.2a1 1 0 0 1 1-.25 11.4 11.4 0 0 0 3.6.57 1 1 0 0 1 1 1V20a1 1 0 0 1-1 1A17 17 0 0 1 3 4a1 1 0 0 1 1-1h3.5a1 1 0 0 1 1 1c0 1.25.2 2.45.57 3.57a1 1 0 0 1-.25 1z" fill="var(--navy)"/></svg>
    <span>+1 555 014 2290</span>
  </div>
  <div class="info" style="top:592px;left:634px">
    <svg width="18" height="14" viewBox="0 0 18 14"><rect x="1" y="1" width="16" height="12" rx="1.5" fill="var(--navy)"/><path d="M1.5 2 L9 8 L16.5 2" stroke="#fff" stroke-width="1.6" fill="none"/></svg>
    <span class="link">HARBORLINESYSTEMS.COM</span>
  </div>
</section>

</body>
</html>
```